Brindle Grass Services website design

We want to create a Sports turf website for our business Brindle Grass Services - we do sports turf management on sports fields around the Mackay region soccer rugby league softball fields etc from full turf management plans and maintenance to just supply and apply of turf management products and just supply of products with program we also do grounds facility maintenance at council facility's and grounds that require a higher level of care - we will up load our logos and fonts etc to assist with the colour pallet for the website - we will have to have a landing page a shop page with tabs a gallery tab along with a grants initiative and our coastals finest green tab also - our font for the txt is called ethnocentric
Updates

how do we open time for people to submit we have no one submitted

Industry/Entity Type

Turf

Coding

Coded - Design and coding required

Number of Pages Required

5+ page

Font styles to use
Other font styles liked:
• ethnocentric

Requirements
Must have
• I have mentioned some waffle in the description that should assist
Should not have
• anything not related

```html
<!DOCTYPE html>
<html lang="en">
<head>
<meta charset="utf-8">
<title>Brindle Grass Services — Elite Sports Turf, Mackay</title>
<link href="https://fonts.googleapis.com/css2?family=Michroma&family=Inter:wght@400;500;600;700&display=swap" rel="stylesheet">
<style>
:root{
  --bg:#0a0f0b;
  --bg-card:#111712;
  --line:#1f2a21;
  --text:#ffffff;
  --muted:#d6dcd6;
  --green:#2fbf4a;
  --green-2:#6dcb3c;
  --badge:#8ff0a4;
  --badge-ink:#0b2a12;
}
*{box-sizing:border-box;margin:0;padding:0}
html,body{width:1141px;height:1200px;overflow:hidden;background:var(--bg);color:var(--text);font-family:"Inter",sans-serif}
.display{font-family:"Michroma",sans-serif;text-transform:uppercase}
.wrap{width:712px;margin-left:214px}
.topbar{height:23px;display:flex;align-items:center;justify-content:center;background:linear-gradient(90deg,#0f2a2e,#0c1a14 60%,#163b1a);font-size:7px;letter-spacing:1.6px}
.nav{height:39px;background:#090d0a;border-bottom:1px solid var(--line)}
.nav .wrap{height:100%;display:flex;align-items:center;justify-content:space-between}
.brand{display:flex;align-items:center;gap:6px;font-family:"Michroma",sans-serif;font-size:9px;color:var(--text)}
.brand-dot{width:8px;height:8px;background:var(--green)}
.nav-links{display:flex;gap:4px;font-size:9.5px}
.nav-links a{color:var(--text);text-decoration:none;padding:5px 8px;border:1px solid transparent;border-radius:5px}
.nav-links a.active{background:#121a13;border-color:#24302a}
.hero{height:337px;background:radial-gradient(ellipse at 90% 0%,rgba(30,70,80,.45),transparent 55%),linear-gradient(180deg,#11291a 0%,#0a0f0b 45%);border-bottom:1px solid var(--line)}
.hero .wrap{display:flex;justify-content:space-between;padding-top:48px}
.hero-copy{width:350px}
.badge{display:inline-block;background:var(--badge);color:var(--badge-ink);font-size:6px;padding:3px 7px;border-radius:8px;letter-spacing:.6px}
.hero h1{font-size:29px;line-height:34px;font-weight:400;letter-spacing:1px;margin-top:2px}
.hero p{font-size:9.5px;line-height:11.5px;margin-top:12px}
.chips{display:flex;flex-wrap:wrap;gap:6px;margin-top:10px;width:320px}
.chip{font-size:8px;border:1px solid #26302a;border-radius:10px;padding:4px 7px;color:var(--muted);background:#0d130e}
.actions{display:flex;gap:8px;margin-top:12px}
.btn{font-size:9.5px;font-weight:600;border-radius:6px;padding:0 11px;height:30px;display:inline-flex;align-items:center;text-decoration:none}
.btn-solid{background:linear-gradient(90deg,var(--green),var(--green-2));color:#06200c}
.btn-line{border:1.5px solid var(--green);color:var(--text)}
.hero-mark{width:349px;margin-top:61px}
.mark-box{height:77px;border:1px solid #26302a;border-radius:8px;background:#0c110d;display:flex;align-items:center;justify-content:center;gap:10px;font-family:"Michroma",sans-serif;font-size:17px}
.mark-box .sq{width:14px;height:14px;background:var(--green)}
.mark-tag{font-size:10px;margin-top:8px;text-align:center;letter-spacing:.3px}
.stats{display:grid;grid-template-columns:repeat(4,1fr);gap:15px;margin-top:38px}
.stat{height:51px;background:var(--bg-card);border:1px solid var(--line);border-radius:7px;padding:10px}
.stat small{display:flex;align-items:center;gap:4px;font-size:9.5px;color:var(--muted)}
.stat strong{display:block;font-size:15px;font-weight:700;margin-top:2px}
.ico{width:8px;height:8px}
.section-title{font-size:17px;font-weight:400;letter-spacing:.6px;margin-top:74px}
.section-lead{font-size:9.5px;line-height:11.5px;margin-top:10px;width:400px}
.programs{display:grid;grid-template-columns:repeat(3,1fr);gap:14px;margin-top:10px}
.card{background:var(--bg-card);border:1px solid var(--line);border-radius:8px;padding:11px}
.programs .card{height:109px}
.card h3{font-family:"Michroma",sans-serif;font-size:9px;font-weight:400;text-transform:uppercase;letter-spacing:.4px}
.card p{font-size:9.5px;line-height:11.5px;color:var(--muted);margin-top:10px}
.price{font-size:9.5px;font-weight:700;margin-top:9px;color:var(--muted)}
.services{display:grid;grid-template-columns:1fr 1fr;gap:14px;margin-top:77px}
.services .card{height:107px}
.services .btn{height:28px;margin-top:9px;font-size:9.5px}
.footer{border-top:1px solid var(--line);margin-top:38px;padding-top:21px}
.footer-grid{border-top:1px solid var(--line);padding-top:20px;display:grid;grid-template-columns:repeat(4,1fr);gap:15px}
.footer-about p{font-size:9.5px;line-height:11.5px;margin-top:10px}
.footer-about .badge{margin-top:9px}
.footer h4{font-size:11px;font-weight:600}
.footer ul{list-style:none;margin-top:6px}
.footer li{font-size:9.5px;padding-left:8px;height:37px;line-height:14px}
.copy{font-size:8px;margin-top:7px}
</style>
</head>
<body>
<div class="topbar display">Performance starts from the ground up</div>
<header class="nav">
  <div class="wrap">
    <div class="brand"><span class="brand-dot"></span>Brindle Grass Services</div>
    <nav class="nav-links">
      <a class="active" href="#">Home</a><a href="#">Shop</a><a href="#">Gallery</a><a href="#">Grants</a><a href="#">Coastal's Finest Green</a><a href="#">About</a><a href="#">Contact</a>
    </nav>
  </div>
</header>

<section class="hero">
  <div class="wrap">
    <div class="hero-copy">
      <span class="badge display">Sports turf specialists</span>
      <h1 class="display">Elite Sports<br>Turf •<br>Mackay</h1>
      <p>From full management plans to supply &amp; apply, we keep soccer, rugby league and softball surfaces game-ready—safe, fast and consistent.</p>
      <div class="chips">
        <span class="chip">Programs</span><span class="chip">Fertiliser &amp; Wetting Agents</span><span class="chip">Weed &amp; Pest</span><span class="chip">Renovations</span><span class="chip">Facility Maintenance</span>
      </div>
      <div class="actions">
        <a class="btn btn-solid" href="#">Shop Products</a>
        <a class="btn btn-line" href="#">View Programs</a>
      </div>
    </div>
    <div class="hero-mark">
      <div class="mark-box"><span class="sq"></span>Brindle Grass Services</div>
      <div class="mark-tag display">Performance starts from the ground up</div>
    </div>
  </div>
</section>

<main class="wrap">
  <div class="stats">
    <div class="stat"><small><svg class="ico" viewBox="0 0 8 8"><circle cx="4" cy="4" r="4" fill="#3ccf3c"/></svg>Surfaces managed</small><strong>40+ fields</strong></div>
    <div class="stat"><small><svg class="ico" viewBox="0 0 8 8"><circle cx="4" cy="3" r="2.5" fill="#e53935"/><path d="M3.5 5h1v3h-1z" fill="#aaa"/></svg>Service area</small><strong>Mackay</strong></div>
    <div class="stat"><small><svg class="ico" viewBox="0 0 8 8"><circle cx="4" cy="4.5" r="3.3" fill="#ddd"/><path d="M4 4.5V2.6" stroke="#333" stroke-width=".8"/></svg>Turnaround</small><strong>Fast</strong></div>
    <div class="stat"><small><svg class="ico" viewBox="0 0 10 10"><path d="M5 0l1.5 3.3 3.5.3-2.7 2.3.9 3.5L5 7.6 1.8 9.4l.9-3.5L0 3.6l3.5-.3z" fill="#f5c518"/></svg>Rating</small><strong>5.0</strong></div>
  </div>

  <h2 class="section-title display">Turf management programs</h2>
  <p class="section-lead">Pick a program that fits your facility—each includes a season-ready plan, site visits, and supply &amp; apply of products as required.</p>
  <div class="programs">
    <article class="card"><h3>Essential Care</h3><p>Monthly visits • Mowing specs • Nutrient program • Wetting agents • Broadleaf &amp; bindii control.</p><div class="price">$</div></article>
    <article class="card"><h3>Performance</h3><p>Fortnightly visits • Renovations • In-season recovery • Pest &amp; disease monitoring • Detailed reporting.</p><div class="price">$$</div></article>
    <article class="card"><h3>Elite</h3><p>Weekly visits • Growth regulation • Sand topdressing • Full renovation plan • Match-day presentation.</p><div class="price">$$$</div></article>
  </div>

  <div class="services">
    <article class="card"><h3>Facility Maintenance</h3><p>Beyond the grass: line marking, irrigation checks, litter &amp; debris removal, safety checks and council-level presentation.</p><a class="btn btn-solid" href="#">Request a Site Visit</a></article>
    <article class="card"><h3>Supply &amp; Apply</h3><p>We can supply products with an endorsed program—or apply them for you. Bulk rates available for clubs and councils.</p><a class="btn btn-line" href="#">Browse Products</a></article>
  </div>
</main>

<footer class="footer">
  <div class="wrap">
    <div class="footer-grid">
      <div class="footer-about">
        <div class="brand"><span class="brand-dot"></span>Brindle Grass Services</div>
        <p>Sports turf management for clubs, schools and councils across Mackay: full programs, supply &amp; apply, and facility care.</p>
        <span class="badge display">QLD • Mackay region</span>
      </div>
      <div><h4>Company</h4><ul><li>About</li><li>Gallery</li><li>Grants</li></ul></div>
      <div><h4>Services</h4><ul><li>Turf Programs</li><li>Facility Maintenance</li><li>Shop</li></ul></div>
      <div><h4>Contact</h4><ul><li>Contact Form</li><li>hello@brindlegrass.com.au</li><li>Social Page</li></ul></div>
    </div>
    <p class="copy">© 2025 Brindle Grass Services. All rights reserved.</p>
  </div>
</footer>
</body>
</html>
```